Powerpoint template for our Credentials presentation for our new consulting business - Brightwell Le

We are a new company called Brightwell Ledger Partners (BLP) based in Sydney Australia

We have both run media buying agencies for many years.

Those agencies run by multi-national organisations are becoming less and less transparent with the transactions that they are managing – clients are being significantly over-charged in many areas – especially digital media.

At the same time, our experience has told us that most clients have little understanding of how media should be planned and bought

We are making ourselves available to those clients who cant afford a full time specialist but want to ensure that they are making the correct media and marketing decisions that benefit them rather than their agency.

Target Market(s)

Marketing Managers and Directors

Industry/Entity Type

Media

Font styles to use
Other font styles liked:
• Font used in our logo (attached)

Colors
33a6d7
fbee3e
ffffff

Requirements
Must have
• We have provided the logo that represents the look and feel of the company.
• Please incorporate these colours - blue, yellow and white - into the powerpoint template

```html
<!DOCTYPE html>
<html lang="en">
<head>
<meta charset="utf-8">
<title>Brightwell Ledger Partners – Credentials Template</title>
<link href="https://fonts.googleapis.com/css2?family=Open+Sans:wght@300;400;600;700&display=swap" rel="stylesheet">
<style>
:root{
  --blue:#2f72b7;
  --blue-deep:#255f9e;
  --yellow:#f7e41b;
  --lime:#b8c93b;
  --white:#ffffff;
  --ink:#222a33;
  --muted:#8a8f96;
  --line:#e3e6ea;
  --page:#d6d6d6;
}
*{margin:0;padding:0;box-sizing:border-box}
html,body{width:1200px;height:2235px;overflow:hidden;background:var(--page);font-family:"Open Sans",Arial,sans-serif;color:var(--ink)}
.deck{position:relative;width:1200px;height:2235px;display:grid;grid-template-columns:585px 585px;grid-template-rows:repeat(5,436px);column-gap:15px;row-gap:10px;padding:7.5px}
.slide{position:relative;overflow:hidden;background:var(--white)}
.abs{position:absolute}
.title{position:absolute;left:30px;top:24px;font-size:24px;font-weight:700;color:var(--blue)}
.title::after{content:"";position:absolute;left:0;bottom:-9px;width:30px;height:4px;background:var(--yellow)}
.brand{position:absolute;display:flex;align-items:center;gap:6px;font-weight:700;font-size:10px;line-height:11px;color:var(--blue)}
.brand .mark{width:31px;height:31px;background:var(--yellow);border:2px solid var(--blue)}
.brand.top{right:12px;top:15px}
.brand.light{color:var(--white)}
.brand.light .mark{background:var(--white);border-color:var(--white)}
.brand.big{font-size:17px;line-height:20px;gap:12px}
.brand.big .mark{width:60px;height:60px;background:transparent;border:3px solid var(--white)}
.footer{position:absolute;left:0;right:0;bottom:0;height:22px;background:var(--blue);color:var(--white);font-size:11px;line-height:22px;padding-left:10px}
.footer small{font-size:8px}
.footer .num{position:absolute;right:25px;top:0;width:24px;height:22px;background:var(--white);color:var(--ink);text-align:center;font-size:10px}
.footer .tab{position:absolute;right:0;top:0;width:25px;height:22px;background:var(--yellow)}
.photo{position:absolute}
.body{font-size:11px;line-height:14px}
/* slide 1 */
.model-sub{position:absolute;left:0;right:0;top:100px;text-align:center;font-size:14px;color:#444}
.step{position:absolute;top:157px;width:105px;height:88px;background:var(--blue);color:var(--white);font-size:12px;display:flex;align-items:center;justify-content:center}
.plus{position:absolute;top:185px;font-size:26px;color:var(--blue);font-weight:300}
.bullets{position:absolute;top:264px;width:105px;font-size:9.5px;line-height:11px;color:#444;padding-left:10px}
.bullets li{margin-bottom:0}
.callout{position:absolute;left:33px;top:358px;font-size:14px;color:var(--blue)}
/* slide 2 */
.offer{position:absolute;left:283px;display:flex;align-items:center;gap:14px;font-size:12.5px;color:#555}
.offer .ico{width:30px;height:30px;border-radius:50%;background:var(--blue);display:flex;align-items:center;justify-content:center}
/* slide 3 */
.quote-mark{position:absolute;left:269px;top:105px;width:54px;height:54px;border-radius:50%;background:var(--yellow);color:var(--blue);font-size:46px;font-weight:700;text-align:center;line-height:68px}
.quote{position:absolute;left:0;right:0;top:190px;text-align:center;color:var(--white);font-size:19px;font-weight:300;line-height:23.5px}
.quote cite{display:block;font-style:normal;font-size:11px;margin-top:12px}
/* slide 4 */
.about{position:absolute;left:292px;top:90px;width:293px;height:249px;background:var(--blue);color:var(--white);padding:18px 18px}
.about h2{font-size:24px;font-weight:600;margin-bottom:16px}
/* slide 5 */
.lede{position:absolute;left:25px;top:112px;font-size:16.5px;font-weight:700;line-height:20px}
.lede span{color:var(--blue)}
.col{position:absolute;top:177px;width:250px;font-size:12px;line-height:15px;color:#a3a7ad}
.col p+p{margin-top:13px}
/* slide 6 */
.panel{position:absolute;left:307px;top:0;width:278px;height:436px;background:var(--blue);color:var(--white)}
.ring{position:absolute;top:148px;width:44px;height:44px;border:2px solid var(--white);border-radius:50%;display:flex;align-items:center;justify-content:center}
/* slide 7 */
.band{position:absolute;left:0;right:0;top:268px;height:107px;background:var(--lime);text-align:center;padding-top:20px}
/* slide 8 */
.pin{position:absolute;width:15px;height:15px;border-radius:50%;background:var(--blue);border:2px solid var(--white)}
/* slide 9 */
.grid{position:absolute;left:22px;top:88px;display:grid;grid-template-columns:repeat(5,108px);grid-template-rows:repeat(4,71px);border-top:1px solid var(--line);border-left:1px solid var(--line)}
.grid div{border-right:1px solid var(--line);border-bottom:1px solid var(--line);display:flex;align-items:center;justify-content:center;text-align:center;font-size:12px;font-weight:700;color:var(--blue)}
/* slide 10 */
.contact-panel{position:absolute;left:30px;top:0;width:240px;height:436px;background:var(--blue-deep);opacity:.96}
.contact{position:absolute;left:60px;display:flex;align-items:center;gap:14px;color:var(--white);font-size:12px}
.social{position:absolute;top:412px;width:17px;height:17px;border-radius:50%;background:#c9c06a}
</style>
</head>
<body>
<main class="deck">

  <!-- Case study -->
  <section class="slide">
    <h1 class="title">Case Study – Education Client</h1>
    <div class="brand top"><span class="mark"></span><span>Brightwell<br>Ledger<br>Partners</span></div>
    <p class="model-sub">Eg Programmatic Partner Selection Model</p>
    <div class="step" style="left:25px">Transparency</div>
    <div class="plus" style="left:139px">+</div>
    <div class="step" style="left:168px">InsightTools</div>
    <div class="plus" style="left:283px">+</div>
    <div class="step" style="left:312px">Performance</div>
    <div class="plus" style="left:427px">+</div>
    <div class="step" style="left:456px">Reporting</div>
    <ul class="bullets" style="left:25px"><li>Transparent model</li><li>Remuneration Offer</li></ul>
    <ul class="bullets" style="left:168px"><li>Different strengths by target</li><li>Data access</li><li>Segmentation</li></ul>
    <ul class="bullets" style="left:312px"><li>Prog performance</li><li>Exceed acquisition benchmarks &amp; KPIs</li></ul>
    <ul class="bullets" style="left:456px;width:115px"><li>Analytics &amp; reporting platform</li><li>Path-to-conversion reporting</li><li>Campaign tags to feed real-time data into custom dashboard/DMP</li></ul>
    <p class="callout">More than halved major Trading Desk margin!!</p>
    <footer class="footer">Brightwell Ledger Partners <small>© 2016. All rights reserved.</small><span class="num">21</span><span class="tab"></span></footer>
  </section>

  <!-- Alignment & integration -->
  <section class="slide">
    <h1 class="title">We deliver alignment &amp; integration</h1>
    <div class="brand top"><span class="mark"></span><span>Brightwell<br>Ledger<br>Partners</span></div>
    <div class="photo" role="img" aria-label="Photo of a smiling team gathered around a laptop" style="left:0;top:90px;width:270px;height:285px;background:linear-gradient(135deg,#e9ecef,#c9ccd0 60%,#f2f2f0)"></div>
    <div class="offer" style="top:102px"><span class="ico"><svg width="14" height="14" viewBox="0 0 14 14"><path d="M7 12 2 7.5A3 3 0 0 1 7 3.5 3 3 0 0 1 12 7.5Z" fill="#fff"/></svg></span>Managed services</div>
    <div class="offer" style="top:148px"><span class="ico"><svg width="14" height="14" viewBox="0 0 14 14"><path d="M3 11 10 4l1.5 1.5-7 7H3Z" fill="#fff"/></svg></span>In-house solution</div>
    <div class="offer" style="top:195px"><span class="ico"><svg width="14" height="14" viewBox="0 0 14 14"><path d="M4 10l6-7-1 5 2 1-6 4 1-3Z" fill="#fff"/></svg></span>Hybrid</div>
    <div class="offer" style="top:241px"><span class="ico"><svg width="14" height="14" viewBox="0 0 14 14"><circle cx="7" cy="7" r="4.5" fill="none" stroke="#fff" stroke-width="2.5" stroke-dasharray="2.5 1.5"/><circle cx="7" cy="7" r="1.6" fill="#fff"/></svg></span>Control partner relationships</div>
    <div class="offer" style="top:289px"><span class="ico"><svg width="14" height="14" viewBox="0 0 14 14"><circle cx="6" cy="6" r="3.5" fill="none" stroke="#fff" stroke-width="1.8"/><path d="M8.5 8.5 12 12" stroke="#fff" stroke-width="2"/></svg></span>Ownership of data</div>
    <div class="offer" style="top:336px"><span class="ico"><svg width="16" height="14" viewBox="0 0 16 14"><circle cx="8" cy="5" r="2.4" fill="#fff"/><circle cx="3.5" cy="6" r="1.8" fill="#fff"/><circle cx="12.5" cy="6" r="1.8" fill="#fff"/><path d="M4 12a4 4 0 0 1 8 0Z" fill="#fff"/></svg></span>Bespoke solutions</div>
    <footer class="footer">Brightwell Ledger Partners <small>© 2016. All rights reserved.</small><span class="num">22</span><span class="tab"></span></footer>
  </section>

  <!-- Quote -->
  <section class="slide" style="background:var(--blue)">
    <div class="photo" role="img" aria-label="Blue-toned photo of a large conference hall with rows of seats" style="inset:0;background:linear-gradient(180deg,#2a5f9c,#3a78bb 55%,#2f6aa9)"></div>
    <div class="quote-mark">“</div>
    <p class="quote">Coming together is a beginning.<br>Keeping together is progress.<br>Working together is success.<cite>- Walter Prentice -</cite></p>
  </section>

  <!-- About us -->
  <section class="slide">
    <div class="photo" role="img" aria-label="Photo of a businessman presenting to colleagues in a bright office" style="inset:0;background:linear-gradient(120deg,#f4f6f8,#d7dbe0 45%,#eef0f2)"></div>
    <div class="brand top" style="background:#fff;padding:3px 4px"><span class="mark"></span><span>Brightwell<br>Ledger<br>Partners</span></div>
    <div class="about">
      <h2>About Us</h2>
      <p class="body">We are Brightwell Ledger Partners Taking Services to a New Level of Excellence</p>
      <p class="body" style="margin-top:12px">Lorem ipsum dolor sit amet, consectetur adipiscing elit, sed do eiusmod tempor incididunt ut labore et dolore magna aliqua. Ut enimad minim veniam, quis nostrud exercitation ullamco laboris nisi ut aliquip ex ea commodo consequat.</p>
    </div>
    <footer class="footer">Brightwell Ledger Partners <small>© 2016. All rights reserved.</small><span class="num">24</span><span class="tab"></span></footer>
  </section>

  <!-- Two column -->
  <section class="slide">
    <h1 class="title">Two Column Description</h1>
    <div class="brand top"><span class="mark"></span><span>Brightwell<br>Ledger<br>Partners</span></div>
    <p class="lede">We are <span>Brightwell Ledger Partners</span><br>Taking Services to a New Level of Excellence</p>
    <div class="col" style="left:25px"><p>Lorem ipsum dolor sit amet, consectetur adipiscing elit, sed do eiusmod tempor incididunt ut labore et dolore magna aliqua. Ut enimad minim veniam, quis nostrud exercitation ullamco laboris nisi ut aliquip ex ea commodo consequat.</p><p>Duis aute irure dolor in reprehenderit in voluptate velit esse cillum dolore eu fugiat nulla pariatur. Excepteur sint occaecat cupidatat non proident, sunt inculpa qui officia deserunt mollit anim id est laborum.</p></div>
    <div class="abs" style="left:300px;top:177px;width:1px;height:200px;background:var(--line)"></div>
    <div class="col" style="left:320px"><p>Lorem ipsum dolor sit amet, consectetur adipiscing elit, sed do eiusmod tempor incididunt ut labore et dolore magna aliqua. Ut enimad minim veniam, quis nostrud exercitation ullamco laboris nisi ut aliquip ex ea commodo consequat.</p><p>Duis aute irure dolor in reprehenderit in voluptate velit esse cillum dolore eu fugiat nulla pariatur. Excepteur sint occaecat cupidatat non proident, sunt inculpa qui officia deserunt mollit anim id est laborum.</p></div>
    <footer class="footer">Brightwell Ledger Partners <small>© 2016. All rights reserved.</small><span class="num">25</span><span class="tab"></span></footer>
  </section>

  <!-- Feature panel -->
  <section class="slide">
    <div class="photo" role="img" aria-label="Photo of a businesswoman holding a cup beside colleagues at a laptop" style="left:0;top:0;width:307px;height:436px;background:linear-gradient(135deg,#eef0f2,#cdd1d6 55%,#e6e4dc)"></div>
    <div class="panel">
      <div class="brand light" style="left:45px;top:45px;font-size:15px;line-height:19px;gap:12px"><span class="mark" style="width:48px;height:48px;background:transparent;border:3px solid #fff"></span><span>Brightwell<br>Ledger<br>Partners</span></div>
      <div class="ring" style="left:13px"><svg width="18" height="18" viewBox="0 0 18 18"><path d="M5 13l8-9-1 6 2 1-8 5 1-3Z" fill="#fff"/></svg></div>
      <div class="ring" style="left:106px"><svg width="18" height="18" viewBox="0 0 18 18"><circle cx="9" cy="8" r="4" fill="#fff"/><path d="M6 12l-1 4 4-2 4 2-1-4" fill="#fff"/></svg></div>
      <div class="ring" style="left:196px"><svg width="20" height="18" viewBox="0 0 20 18"><path d="M3 14 2 5l5 4 3-6 3 6 5-4-1 9Z" fill="none" stroke="#fff" stroke-width="1.8"/></svg></div>
      <div class="abs" style="left:13px;top:218px;width:252px;height:1px;background:rgba(255,255,255,.6)"></div>
      <h2 class="abs" style="left:20px;top:250px;font-size:16.5px;font-weight:700">Your Title Goes Here</h2>
      <p class="abs body" style="left:20px;top:286px;width:240px;font-size:10.5px;line-height:12.5px">Lorem ipsum dolor sit amet, consectetur adipiscing elit, sed do eiusmod tempor incididunt ut labore et dolore magna aliqua. Duis aute irure dolor in reprehenderit in voluptate velit esse cillum dolore.</p>
      <div class="abs" style="left:0;right:0;bottom:0;height:42px;background:var(--yellow);color:var(--blue);font-size:13px;text-align:center;line-height:42px">Brightwell Ledger Partners</div>
    </div>
  </section>

  <!-- Divider -->
  <section class="slide" style="background:var(--blue)">
    <div class="photo" role="img" aria-label="Blue-toned photo of business people talking around a table" style="inset:0;background:linear-gradient(180deg,#2f68a6,#3c7bbd 50%,#2c63a0)"></div>
    <div class="brand big light" style="left:213px;top:117px"><span class="mark"></span><span>Brightwell<br>Ledger<br>Partners</span></div>
    <div class="band">
      <p style="color:#fff;font-size:12px;font-weight:700">Divider Page</p>
      <p style="color:var(--blue);font-size:22px;font-weight:700;line-height:28px">Your Title Goes Here</p>
      <p style="color:#fff;font-size:14px">Your Subtitle Here</p>
    </div>
  </section>

  <!-- Global -->
  <section class="slide">
    <h1 class="title">Global Experience</h1>
    <div class="brand top"><span class="mark"></span><span>Brightwell<br>Ledger<br>Partners</span></div>
    <div class="photo" role="img" aria-label="Grey world map showing office locations" style="left:90px;top:105px;width:475px;height:270px;background:radial-gradient(ellipse at 50% 45%,#d6d6d6,#e6e6e6 60%,#fff 80%)"></div>
    <span class="pin" style="left:181px;top:206px"></span>
    <span class="pin" style="left:295px;top:172px"></span>
    <span class="pin" style="left:373px;top:211px"></span>
    <span class="pin" style="left:502px;top:199px"></span>
    <span class="pin" style="left:452px;top:247px"></span>
    <span class="pin" style="left:245px;top:281px"></span>
    <span class="pin" style="left:325px;top:301px"></span>
    <span class="pin" style="left:517px;top:301px"></span>
    <span class="pin" style="left:25px;top:296px;width:22px;height:22px"></span>
    <p class="abs" style="left:57px;top:292px;width:100px;font-size:10px;line-height:12px;color:#777">Lorem ipsum dolor sit amet, consectetur adipiscing elit, sed do eiusmod tempor incididunt ut labore et dolore magna aliqua.</p>
    <footer class="footer">Brightwell Ledger Partners <small>© 2016. All rights reserved.</small><span class="num">27</span><span class="tab"></span></footer>
  </section>

  <!-- Portfolio -->
  <section class="slide">
    <h1 class="title">Sample Customer Portfolio</h1>
    <div class="brand top"><span class="mark"></span><span>Brightwell<br>Ledger<br>Partners</span></div>
    <div class="grid">
      <div>Corvale</div><div>Lumentra</div><div>Veltrano</div><div>Kestrel</div><div>Ardent Tyre</div>
      <div>Sola Skin</div><div>Northline Cable</div><div>Farpoint</div><div>Polaris Resin</div><div>Tidewell Energy</div>
      <div>Signal Barn</div><div>Brantel</div><div>Harvest Foods</div><div>Ridgeway Tyres</div><div>Orchard Grill</div>
      <div>Daemar</div><div>Linwood Hale</div><div>Stonebrook</div><div>Meridian Bank</div><div>Regent Capital</div>
    </div>
    <footer class="footer">Brightwell Ledger Partners <small>© 2016. All rights reserved.</small><span class="num">29</span><span class="tab"></span></footer>
  </section>

  <!-- Thank you -->
  <section class="slide" style="background:var(--blue)">
    <div class="photo" role="img" aria-label="Blue-toned photo of a city street lined with tall buildings" style="inset:0;background:linear-gradient(90deg,#3a74b4,#4f86c2 60%,#3a72b1)"></div>
    <div class="contact-panel"></div>
    <div class="brand big light" style="left:65px;top:50px;font-size:15px;line-height:19px"><span class="mark" style="width:52px;height:52px"></span><span>Brightwell<br>Ledger<br>Partners</span></div>
    <h2 class="abs" style="left:48px;top:163px;color:#fff;font-size:19px;font-weight:400">Our Contact</h2>
    <div class="abs" style="left:48px;top:194px;width:210px;height:1px;background:rgba(255,255,255,.6)"></div>
    <div class="contact" style="top:222px"><svg width="16" height="14" viewBox="0 0 16 14"><path d="M8 1 1 7h2v6h4V9h2v4h4V7h2Z" fill="#fff"/></svg>123 Your Street, City 12345</div>
    <div class="contact" style="top:262px"><svg width="16" height="14" viewBox="0 0 16 14"><path d="M3 1h3l1 3-2 1.5a8 8 0 0 0 4 4L10.5 8l3 1v3a2 2 0 0 1-2 2C6 14 1 9 1 3a2 2 0 0 1 2-2Z" fill="#fff"/></svg>(123) 456-7890</div>
    <div class="contact" style="top:303px"><svg width="16" height="14" viewBox="0 0 16 14"><rect x="1" y="2" width="14" height="10" fill="#fff"/><path d="M1 2l7 6 7-6" fill="none" stroke="#255f9e" stroke-width="1.2"/></svg>hello@brightwell.example</div>
    <div class="contact" style="top:344px"><svg width="16" height="14" viewBox="0 0 16 14"><circle cx="8" cy="7" r="6" fill="#fff"/><path d="M2 7h12M8 1c-3 3-3 9 0 12M8 1c3 3 3 9 0 12" fill="none" stroke="#255f9e" stroke-width="1"/></svg>www.brightwell.example</div>
    <div class="abs" style="left:30px;top:405px;width:240px;height:31px;background:var(--yellow)"></div>
    <span class="social" style="left:115px"></span><span class="social" style="left:141px"></span><span class="social" style="left:167px"></span>
    <h2 class="abs" style="left:300px;width:270px;top:184px;text-align:center;color:#fff;font-size:36px;font-weight:700">THANK YOU</h2>
    <p class="abs" style="left:300px;width:270px;top:232px;text-align:center;color:#fff;font-size:13px">For Your Precious Time</p>
  </section>

</main>
</body>
</html>
```